Website Design for a Party Rental
Brinmore Party Rentals
Project: Website Design for a Party Rental
Website Design for a Party Rental - Events
Creative Brief
Events
http://www.brinmorepartyrentals-example.com/
Its a family owned party rental company, that rents from chairs, table, linen, china, flatware, to tenting, dance floor & lighting. We rent for any sort of event, from casual birthday parties, wedding, to the Pacific Motorwheel Expo in Harbin Dome Arena. Our prices are cheaper than our nearby competitors. We do free consultations on site, therefore providing a quote if client wishes to confirm with us.
Likes: Oak & Meadow Rentals http://www.oakandmeadoweventhire-example.com/ We Like the Inventory Layout of this website, and how its organized. Also, the Slide show above the header.
Modern
Cobalt Blue (Its like a Ocean/Royal Blue)
http://www.oakandmeadoweventhire-example.com/
http://losangeles.vintelpartyhire-example.com/

```html
<!DOCTYPE html>
<html lang="en">
<head>
<meta charset="utf-8">
<title>Brinmore Party Rentals</title>
<link href="https://fonts.googleapis.com/css2?family=PT+Serif:ital,wght@0,400;0,700;1,400;1,700&display=swap" rel="stylesheet">
<style>
:root{
  --page-bg:#1c2233;
  --panel:#ffffff;
  --navy:#1e3658;
  --cobalt:#2c5a96;
  --cobalt-light:#5b86bf;
  --grey-text:#8a8c90;
  --box:#3c3f44;
  --box-dark:#2b2d31;
  --footer:#26282c;
  --footer-line:#3a3c41;
  --footer-text:#c9cbcf;
  --white:#ffffff;
}
*{margin:0;padding:0;box-sizing:border-box}
html,body{width:1200px;height:1096px;overflow:hidden}
body{
  background:radial-gradient(ellipse at 50% 40%,#27304a 0%,var(--page-bg) 70%);
  font-family:"PT Serif",Georgia,serif;
  position:relative;
}
.site{position:absolute;left:126px;top:0;width:972px;height:1096px;background:var(--panel)}
.brand{position:absolute;left:20px;top:240px;width:420px;text-align:center}
.brand-mark{width:120px;height:120px;border-radius:50%;background:var(--navy);margin:0 auto 30px;position:relative;top:-190px;margin-bottom:-120px}
.brand-name{font-size:35px;font-weight:700;color:var(--navy);white-space:nowrap}
.brand-phone{margin-top:36px;font-size:50px;color:var(--grey-text);letter-spacing:3px}
.utility{position:absolute;left:440px;top:34px;width:500px;display:flex;align-items:center;gap:20px}
.utility a{font-size:17px;color:var(--navy);text-decoration:none;font-weight:700}
.utility a.active{background:#e6e8ec;padding:2px 8px}
.search{margin-left:10px;flex:1;height:26px;border:1px solid #c7c9cd;font-size:14px;color:#888;padding:3px 8px;display:flex;justify-content:space-between;align-items:center}
.slide{position:absolute;left:438px;top:72px;width:522px;height:354px;border:5px solid var(--navy);
  background:linear-gradient(160deg,#5c3a22 0%,#b9865a 30%,#efe3d0 55%,#d9c4a5 75%,#6b4a2d 100%)}
.slide-dots{position:absolute;left:610px;top:416px;display:flex;gap:22px}
.slide-dots span{width:11px;height:11px;border-radius:50%;background:var(--cobalt-light)}
.slide-dots span.on{background:var(--navy)}
.swoosh{position:absolute;left:0;top:430px;width:972px;height:60px}
.main-nav{position:absolute;left:80px;top:452px;display:flex;gap:16px;font-size:35px;color:var(--navy)}
.main-nav a{color:var(--navy);text-decoration:none}
.main-nav a.current{color:var(--cobalt);font-weight:700;text-decoration:underline;text-underline-offset:6px}
.main-nav .sep{color:var(--navy)}
.intro{position:absolute;left:0;top:520px;width:972px;height:358px;border-radius:10px;
  background:linear-gradient(180deg,var(--box) 0%,var(--box-dark) 100%);color:var(--white);text-align:center;padding:22px 50px}
.intro h1{font-size:34px;font-variant:small-caps;font-weight:700;letter-spacing:.5px}
.intro .lead{font-size:20px;line-height:28px;margin-top:8px}
.intro h2{font-size:27px;font-variant:small-caps;font-weight:400;margin-top:20px}
.intro .body{font-size:19.5px;line-height:28px;margin-top:4px}
.footer{position:absolute;left:0;top:898px;width:972px;height:198px;background:var(--footer)}
.footer-nav{display:flex;gap:40px;padding:16px 26px;font-size:15px;font-variant:small-caps;letter-spacing:2px;color:#8d9096;border-bottom:1px solid var(--footer-line)}
.footer-nav .current{color:var(--white);font-weight:700}
.newsletter{position:absolute;left:26px;top:62px;width:290px}
.newsletter h3{font-size:14px;font-weight:400;letter-spacing:2px;font-variant:small-caps;color:var(--footer-text);border-bottom:1px solid var(--footer-line);padding-bottom:4px}
.signup{display:flex;align-items:center;gap:6px;margin-top:8px}
.social{width:22px;height:22px;border-radius:4px;background:var(--cobalt-light)}
.signup .label{font-size:14px;color:var(--footer-text);letter-spacing:2px;margin-left:auto}
.signup-row{display:flex;margin-top:8px}
.signup-row .field{width:250px;height:24px;background:var(--white)}
.signup-row .go{width:26px;height:24px;background:var(--cobalt)}
.contact{position:absolute;left:430px;top:70px;width:200px;text-align:right;font-style:italic;font-size:12px;line-height:17px;color:var(--footer-text)}
.recent{position:absolute;left:716px;top:58px;width:240px}
.recent h3{font-style:italic;font-size:22px;font-weight:400;color:var(--white);text-align:center}
.thumbs{display:grid;grid-template-columns:repeat(3,68px);gap:6px;justify-content:center;margin-top:6px}
.thumbs span{height:46px;border:1px solid #555}
</style>
</head>
<body>
<div class="site">
  <div class="brand">
    <div class="brand-mark"></div>
    <div class="brand-name">Brinmore Party Rentals</div>
    <div class="brand-phone">310·555·0148</div>
  </div>

  <nav class="utility">
    <a href="#" class="active">About us</a>
    <a href="#">Portfolio</a>
    <a href="#">Blog</a>
    <div class="search"><span>Search our website</span>
      <svg width="14" height="14" viewBox="0 0 14 14"><circle cx="5.5" cy="5.5" r="4" fill="none" stroke="#555" stroke-width="2"/><line x1="8.5" y1="8.5" x2="13" y2="13" stroke="#555" stroke-width="2"/></svg>
    </div>
  </nav>

  <div class="slide" role="img" aria-label="Slideshow photo of an event hall set with long banquet tables, white linens and chairs"></div>
  <div class="slide-dots"><span class="on"></span><span></span><span></span><span></span><span></span></div>

  <svg class="swoosh" viewBox="0 0 972 60" preserveAspectRatio="none">
    <path d="M0 22 Q486 -4 972 22 L972 34 Q486 10 0 34 Z" fill="var(--navy)"/>
    <path d="M0 38 Q486 16 972 38" fill="none" stroke="var(--cobalt-light)" stroke-width="3"/>
  </svg>

  <nav class="main-nav">
    <a href="#" class="current">Home</a><span class="sep">|</span>
    <a href="#">Services</a><span class="sep">|</span>
    <a href="#">Catalog</a><span class="sep">|</span>
    <a href="#">Price list</a><span class="sep">|</span>
    <a href="#">Contact us</a>
  </nav>

  <section class="intro">
    <h1>Let Our Wide Range of Rentals Help Your Event!</h1>
    <p class="lead">When it comes to party rentals Los Angeles knows how to get it done!<br>You can count on Brinmore Party Rentals to outfit your event with style. Give us a call today!</p>
    <h2>We'll Outfit Your Event with Quality Party Rentals in Los Angeles.</h2>
    <p class="body">At Brinmore Party Rentals, we pride ourselves on offering the best customer service, as well as the best rental products to the residents of Los Angeles. When it comes to party rentals in Los Angeles, we know that there is a high standard regarding how events should be pulled off. At the same time, we also understand that not everyone has the budget to spend big bucks. We offer the products that are still elegant, but competitively priced.</p>
  </section>

  <footer class="footer">
    <nav class="footer-nav">
      <span class="current">Home</span><span>Services</span><span>Catalog</span><span>Price list</span><span>Contact us</span><span>About us</span><span>Portfolio</span><span>Blog</span>
    </nav>
    <div class="newsletter">
      <h3>Subscribe to our newsletter</h3>
      <div class="signup"><span class="social"></span><span class="social"></span><span class="social"></span><span class="label">Email address</span></div>
      <div class="signup-row"><span class="field"></span><span class="go"></span></div>
    </div>
    <address class="contact">
      4410 Harbor Ave<br>Los Angeles, CA 90021<br><br>
      Monday – Friday: 8 am – 6 pm<br>Saturday: 9 am – 5 pm<br>Sunday Closed
    </address>
    <div class="recent">
      <h3>Recent parties</h3>
      <div class="thumbs">
        <span role="img" aria-label="Party photo" style="background:linear-gradient(#7a4a7e,#c98fb0)"></span>
        <span role="img" aria-label="Party photo" style="background:linear-gradient(#c7b9a4,#8a6e50)"></span>
        <span role="img" aria-label="Party photo" style="background:linear-gradient(#b23a3a,#e0a070)"></span>
        <span role="img" aria-label="Party photo" style="background:linear-gradient(#3a5a8a,#a8c0dd)"></span>
        <span role="img" aria-label="Party photo" style="background:linear-gradient(#d8cfc0,#9b8a70)"></span>
        <span role="img" aria-label="Party photo" style="background:linear-gradient(#5a2e4a,#c7607e)"></span>
      </div>
    </div>
  </footer>
</div>
</body>
</html>
```